New product launches for online boutique

We are looking for an email template, social media template for whenever we launch s new product. We are an online boutique for black women. Imagery should be of black women, use of our logo and a spot to highlight new products and areas for a description of new products.
Template for email marketing
Template for Facebook
Template for Instagram
There could be more than one product being launched
Must be able to sell
Include pricing

Target Market(s)

Black women, women of colour, ages 18-30,

Industry/Entity Type

Skin Care

Requirements
Must have
• Company logo, area for products image, area for products description, must be bright clear

```html
<!DOCTYPE html>
<html lang="en">
<head>
<meta charset="utf-8">
<title>Nuvelle – New Products Email</title>
<link href="https://fonts.googleapis.com/css2?family=Archivo+Narrow:wght@400;500;600;700&family=Poiret+One&display=swap" rel="stylesheet">
<style>
  :root{
    --page:#edeaeb;
    --card:#ffffff;
    --ink:#2e2e2e;
    --muted:#666264;
    --line:#d9d6d6;
    --gold:#c9a04e;
    --dark-panel:#2a2523;
    --sale-panel:#3e3d3d;
    --link-red:#d8334a;
    --icon:#7b7b7b;
  }
  *{box-sizing:border-box;margin:0;padding:0}
  html,body{width:1200px;height:2692px;overflow:hidden}
  body{background:var(--page);font-family:"Archivo Narrow",sans-serif;color:var(--ink);position:relative}
  .abs{position:absolute}

  .preheader{left:0;width:1200px;top:70px;text-align:center;font-size:22px;color:#4a4a4a;line-height:1.2}
  .preheader a{display:inline-block;margin-top:4px;color:var(--link-red);text-decoration:underline}

  .card{left:229px;top:148px;width:740px;height:2335px;background:var(--card);border-radius:22px;overflow:hidden}

  /* header */
  .brand{display:flex;align-items:center;gap:10px;font-weight:600;color:var(--gold);font-size:40px;letter-spacing:2px}
  .brand-dot{width:14px;height:14px;border-radius:50%;background:var(--gold)}
  .header-brand{left:34px;top:52px}
  .header-contact{right:30px;top:56px;display:flex;align-items:center;gap:12px;font-size:19px;color:#555}
  .header-contact .item{display:flex;align-items:center;gap:10px;margin-left:22px}
  .circle-icon{width:38px;height:38px;border:2px solid #8a8a8a;border-radius:50%;display:flex;align-items:center;justify-content:center}

  /* hero */
  .hero{left:0;top:142px;width:740px;height:453px}
  .hero-photo{left:0;top:0;width:391px;height:453px;background:linear-gradient(135deg,#f1efea 0%,#d7d2c9 55%,#8b7868 100%)}
  .hero-panel{left:391px;top:0;width:349px;height:453px;background:linear-gradient(180deg,#241f1d,#3a302b 60%,#1e1a18)}
  .hero-frame{left:358px;top:87px;width:283px;height:283px;border:2px solid var(--gold)}
  .hero-title{left:408px;top:290px;font-family:"Poiret One",sans-serif;font-size:60px;color:#fff}

  /* features */
  .feature{top:672px;width:200px}
  .feature svg{display:block;height:60px}
  .feature h3{margin-top:26px;font-size:22px;font-weight:600;color:#444}
  .feature p{margin-top:6px;font-size:18px;color:#555}

  /* section heads */
  .section-head{left:30px;width:680px;display:flex;justify-content:space-between;align-items:flex-end;border-bottom:2px solid var(--line);padding-bottom:10px}
  .section-head .title{font-size:22px;font-weight:700;letter-spacing:1px}
  .section-head .side{font-size:20px;color:#555}
  .section-head .sub{font-size:20px;color:#444}
  .section-head .side-bold{font-size:22px;font-weight:700;letter-spacing:1px}

  /* offer */
  .offer-photo{left:30px;top:962px;width:295px;height:283px;background:linear-gradient(160deg,#e8b9c2 0%,#d99aa6 40%,#2a9a8c 75%,#1e8a7c 100%)}
  .offer-copy{left:356px;top:970px;width:350px}
  .offer-copy h4{font-size:23px;font-weight:600;color:#444}
  .offer-copy p{margin-top:10px;font-size:18px;line-height:28px;color:#555}
  .btn-outline{display:inline-block;margin-top:14px;width:146px;height:62px;line-height:58px;text-align:center;border:2px solid #c8c5c5;font-size:19px;color:#444;letter-spacing:.5px}
  .offer-copy .accent{margin-top:22px;font-size:22px;color:var(--gold);font-weight:500}
  .offer-copy .accent + p{margin-top:6px}

  /* products */
  .product-photo{top:1368px;width:211px;height:203px}
  .shoe-1{left:30px;background:linear-gradient(160deg,#f3c9cf,#eab3bc 60%,#e4dde0)}
  .shoe-2{left:266px;background:linear-gradient(180deg,#f2f0ee,#d9cbbf 60%,#3a2e29)}
  .shoe-3{left:499px;background:linear-gradient(180deg,#8b5e44,#c79a78 55%,#cdb79b)}
  .product-info{top:1598px}
  .product-info h5{font-size:20px;font-weight:700;color:#444;letter-spacing:.3px}
  .product-info p{margin-top:6px;font-size:18px;color:#555}
  .cart-box{top:1594px;width:50px;height:50px;border:2px solid #c9c6c6;display:flex;align-items:center;justify-content:center}

  /* sale */
  .sale-photo{left:0;top:1707px;width:351px;height:297px;background:linear-gradient(120deg,#e9e4df,#d6c8b8 55%,#b89a74)}
  .sale-panel{left:351px;top:1707px;width:389px;height:297px;background:var(--sale-panel)}
  .sale-copy{left:389px;top:1755px;color:#fff}
  .sale-copy .kicker{font-size:21px;font-weight:700;letter-spacing:.5px}
  .sale-copy .big{font-size:58px;font-weight:700;color:var(--gold);line-height:1;margin-top:6px}
  .sale-copy .off{font-size:29px;font-weight:700;margin-top:8px}
  .sale-btn{display:inline-block;margin-top:18px;width:200px;height:60px;line-height:56px;text-align:center;border:2px solid var(--gold);color:var(--gold);font-size:19px}

  /* footer */
  .footer-brand{left:168px;top:2092px;font-size:34px}
  .social{top:2160px;width:44px;height:44px;border:2px solid #888;border-radius:50%}
  .footer-divider{left:389px;top:2068px;width:2px;height:141px;background:var(--line)}
  .footer-contact{left:454px;top:2082px;font-size:17px;color:#555;line-height:24px}
  .footer-contact .row{display:flex;align-items:flex-start;gap:14px;margin-bottom:8px}
  .footer-contact svg{flex:none;margin-top:3px}
  .copyright{left:0;width:740px;top:2256px;text-align:center;font-size:19px;color:#555}
</style>
</head>
<body>
  <div class="abs preheader">Is this email not displaying correctly?<br><a href="#">View it in your browser.</a></div>

  <main class="abs card">
    <header>
      <div class="abs brand header-brand"><span class="brand-dot"></span>Nuvelle</div>
      <div class="abs header-contact">
        <span class="item">800-5550142
          <span class="circle-icon"><svg width="20" height="20" viewBox="0 0 24 24" fill="none" stroke="#777" stroke-width="2"><path d="M5 3h4l2 5-3 2a12 12 0 0 0 6 6l2-3 5 2v4a2 2 0 0 1-2 2A17 17 0 0 1 3 5a2 2 0 0 1 2-2z"/></svg></span></span>
        <span class="item">hello@nuvelle.shop
          <span class="circle-icon"><svg width="20" height="16" viewBox="0 0 24 18" fill="none" stroke="#777" stroke-width="2"><rect x="1" y="1" width="22" height="16" rx="2"/><path d="M1 2l11 8 11-8"/></svg></span></span>
      </div>
    </header>

    <section class="abs hero">
      <div class="abs hero-photo" role="img" aria-label="Photo of a model in a white lace top and white sunglasses"></div>
      <div class="abs hero-panel" role="img" aria-label="Dim boutique interior with product shelves"></div>
      <div class="abs hero-frame"></div>
      <div class="abs hero-title">Products</div>
    </section>

    <section class="features">
      <div class="abs feature" style="left:61px">
        <svg viewBox="0 0 60 60" width="60" fill="none" stroke="var(--icon)" stroke-width="2.5"><rect x="3" y="3" width="24" height="24"/><rect x="33" y="3" width="24" height="24"/><rect x="3" y="33" width="24" height="24"/><rect x="33" y="33" width="24" height="24"/></svg>
        <h3>Large Collection</h3><p>Read More »</p>
      </div>
      <div class="abs feature" style="left:297px">
        <svg viewBox="0 0 70 60" width="70" fill="none" stroke="var(--icon)" stroke-width="2.5"><rect x="4" y="22" width="62" height="34" rx="2"/><circle cx="35" cy="39" r="10"/><path d="M35 33v12M32 36h5a2 2 0 0 1 0 4h-4a2 2 0 0 0 0 4h5"/><circle cx="28" cy="12" r="8"/><circle cx="44" cy="12" r="8"/></svg>
        <h3>Secure Payments</h3><p>Read More »</p>
      </div>
      <div class="abs feature" style="left:558px">
        <svg viewBox="0 0 70 60" width="70" fill="none" stroke="var(--icon)" stroke-width="2.5"><rect x="4" y="24" width="38" height="24"/><path d="M42 32h12l8 9v7H42z"/><circle cx="16" cy="52" r="5"/><circle cx="52" cy="52" r="5"/><circle cx="30" cy="12" r="9"/><path d="M26 12l3 3 5-6"/></svg>
        <h3>Fast Delivery</h3><p>Read More »</p>
      </div>
    </section>

    <div class="abs section-head" style="top:895px"><span class="title">SPECIAL OFFERS</span><span class="side">More offers</span></div>

    <section>
      <div class="abs offer-photo" role="img" aria-label="Photo of a model in a straw hat and teal shirt"></div>
      <div class="abs offer-copy">
        <h4>Leather Hats</h4>
        <p>Our woven leather style belts can add a<br>new dimension to your outfit.</p>
        <a class="btn-outline">SHOP NOW »</a>
        <p class="accent">New Arrivals</p>
        <p>Be one of the firsts to Discover the New<br>Arrivals.</p>
      </div>
    </section>

    <div class="abs section-head" style="top:1318px"><span class="sub">New collections</span><span class="side-bold">BROWSE STORE</span></div>

    <section class="products">
      <div class="abs product-photo shoe-1" role="img" aria-label="White sneakers on a pink background"></div>
      <div class="abs product-photo shoe-2" role="img" aria-label="Black strappy block heels"></div>
      <div class="abs product-photo shoe-3" role="img" aria-label="Tan lace-up high heels"></div>

      <div class="abs product-info" style="left:30px"><h5>FOOTWARE</h5><p>$15,00 - $25,00</p></div>
      <div class="abs product-info" style="left:266px"><h5>MARLO HEELS</h5><p>$15,00 - $25,00</p></div>
      <div class="abs product-info" style="left:499px"><h5>HIGH HEELS</h5><p>$15,00 - $25,00</p></div>

      <div class="abs cart-box" style="left:191px"><svg width="28" height="24" viewBox="0 0 28 24" fill="none" stroke="#999" stroke-width="2"><path d="M1 2h4l3 14h15l3-10H7"/><circle cx="10" cy="21" r="2"/><circle cx="21" cy="21" r="2"/></svg></div>
      <div class="abs cart-box" style="left:426px"><svg width="28" height="24" viewBox="0 0 28 24" fill="none" stroke="#999" stroke-width="2"><path d="M1 2h4l3 14h15l3-10H7"/><circle cx="10" cy="21" r="2"/><circle cx="21" cy="21" r="2"/></svg></div>
      <div class="abs cart-box" style="left:660px"><svg width="28" height="24" viewBox="0 0 28 24" fill="none" stroke="#999" stroke-width="2"><path d="M1 2h4l3 14h15l3-10H7"/><circle cx="10" cy="21" r="2"/><circle cx="21" cy="21" r="2"/></svg></div>
    </section>

    <section class="sale">
      <div class="abs sale-photo" role="img" aria-label="Photo of a model in a white top beside dried pampas grass"></div>
      <div class="abs sale-panel"></div>
      <div class="abs sale-copy">
        <div class="kicker">SHOP YOUR SIZE</div>
        <div class="big">SALE</div>
        <div class="off">UP TO 75% OFF</div>
        <a class="sale-btn">LET'S SHOP NOW »</a>
      </div>
    </section>

    <footer>
      <div class="abs brand footer-brand"><span class="brand-dot"></span>Nuvelle</div>
      <span class="abs social" style="left:134px"></span>
      <span class="abs social" style="left:185px"></span>
      <span class="abs social" style="left:236px"></span>
      <span class="abs social" style="left:287px"></span>
      <div class="abs footer-divider"></div>
      <div class="abs footer-contact">
        <div class="row"><svg width="16" height="20" viewBox="0 0 16 20" fill="none" stroke="#777" stroke-width="1.8"><path d="M8 19s6-6.5 6-11A6 6 0 0 0 2 8c0 4.5 6 11 6 11z"/><circle cx="8" cy="8" r="2.2"/></svg><span>412 Marigold Ave<br>Fairview, GA 30412</span></div>
        <div class="row"><svg width="18" height="18" viewBox="0 0 24 24" fill="none" stroke="#777" stroke-width="2"><path d="M5 3h4l2 5-3 2a12 12 0 0 0 6 6l2-3 5 2v4a2 2 0 0 1-2 2A17 17 0 0 1 3 5a2 2 0 0 1 2-2z"/></svg><span>Phone: (404) 555-0178</span></div>
        <div class="row"><svg width="18" height="14" viewBox="0 0 24 18" fill="none" stroke="#777" stroke-width="2"><rect x="1" y="1" width="22" height="16" rx="2"/><path d="M1 2l11 8 11-8"/></svg><span>care@nuvelle.shop</span></div>
      </div>
      <div class="abs copyright">© 2019 Nuvelle Beauty. All Rights Reserved</div>
    </footer>
  </main>
</body>
</html>
```